https://dorvakel.com

We need a cool technology design for our Managed IT Services company. We are located in Coral Springs Florida. We provide all IT services and support for small to medium sized businesses. We would like to see designs that use our blue and white colors from our website.

```html
<!DOCTYPE html>
<html lang="en">
<head>
<meta charset="utf-8">
<title>Dorvakel Business Card</title>
<link href="https://fonts.googleapis.com/css2?family=Open+Sans:wght@600;700&family=Arimo:wght@400;700&display=swap" rel="stylesheet">
<style>
  :root {
    --backdrop: #e4e6ea;
    --card-white: #ffffff;
    --card-shade: #eef0f3;
    --navy: #0d2c5a;
    --arc-grey: #a9adb3;
    --on-navy: #e9edf3;
    --on-navy-soft: #b9c4d4;
  }
  * { margin: 0; padding: 0; box-sizing: border-box; }
  html, body { width: 1200px; height: 997px; overflow: hidden; }
  body {
    background: var(--backdrop);
    position: relative;
    font-family: "Arimo", Arial, sans-serif;
  }
  .card {
    position: absolute;
    top: 340px;
    width: 520px;
    height: 300px;
    background: linear-gradient(160deg, var(--card-white) 40%, var(--card-shade));
    box-shadow: 0 10px 30px rgba(0,0,0,0.18);
    overflow: hidden;
  }
  .card--back { left: 50px; }
  .card--front { left: 630px; }
  .card svg.card__art { position: absolute; inset: 0; }
  .wordmark {
    position: absolute;
    left: 0; right: 0;
    text-align: center;
    font-family: "Open Sans", Arial, sans-serif;
    font-weight: 700;
    color: var(--navy);
    letter-spacing: 1px;
  }
  .card--back .wordmark { top: 70px; font-size: 60px; }
  .card--front .wordmark { top: 50px; font-size: 54px; }
  .web-address {
    position: absolute;
    left: 220px;
    top: 266px;
    font-size: 14px;
    line-height: 18px;
    letter-spacing: 3px;
    white-space: nowrap;
    color: var(--on-navy);
    font-weight: 700;
    transform: rotate(-17deg);
    transform-origin: left top;
  }
  .holder {
    position: absolute;
    left: 60px;
    top: 212px;
    width: 190px;
    text-align: center;
    color: var(--on-navy);
  }
  .holder__name { font-weight: 700; font-size: 15px; letter-spacing: 0.5px; }
  .holder__role { font-size: 14px; color: var(--on-navy-soft); margin-top: 2px; }
  .divider {
    position: absolute;
    left: 268px;
    top: 180px;
    width: 1px;
    height: 95px;
    background: var(--on-navy-soft);
    opacity: 0.7;
  }
  .contacts {
    position: absolute;
    left: 288px;
    top: 178px;
    list-style: none;
    color: var(--on-navy);
    font-size: 15px;
  }
  .contacts li { display: flex; align-items: center; gap: 12px; height: 26px; }
  .contacts svg { width: 16px; height: 16px; flex: none; }
</style>
</head>
<body>

  <section class="card card--back" aria-label="Card back">
    <svg class="card__art" viewBox="0 0 520 300" width="520" height="300" aria-hidden="true">
      <path d="M40 300 Q250 240 520 120" fill="none" stroke="var(--arc-grey)" stroke-width="3"/>
      <path d="M70 300 Q270 250 520 140 L520 300 Z" fill="var(--navy)"/>
    </svg>
    <div class="wordmark">DORVAKEL</div>
    <div class="web-address">www.dorvakel.com</div>
  </section>

  <section class="card card--front" aria-label="Card front">
    <svg class="card__art" viewBox="0 0 520 300" width="520" height="300" aria-hidden="true">
      <path d="M20 185 Q260 100 515 118" fill="none" stroke="var(--arc-grey)" stroke-width="3"/>
      <path d="M0 205 Q250 120 520 140 L520 300 L0 300 Z" fill="var(--navy)"/>
    </svg>
    <div class="wordmark">DORVAKEL</div>

    <div class="holder">
      <div class="holder__name">LENA MARSH</div>
      <div class="holder__role">Director</div>
    </div>
    <div class="divider"></div>
    <ul class="contacts">
      <li>
        <svg viewBox="0 0 16 16"><circle cx="8" cy="8" r="8" fill="var(--on-navy)"/><path d="M5 4.5h2l.6 2-1 .8a5 5 0 0 0 2.1 2.1l.8-1 2 .6v2c-3.5.3-6.8-3-6.5-6.5z" fill="var(--navy)"/></svg>
        555 210 4830
      </li>
      <li>
        <svg viewBox="0 0 16 16"><circle cx="8" cy="8" r="8" fill="var(--on-navy)"/><rect x="5.5" y="3.5" width="5" height="9" rx="1" fill="var(--navy)"/><rect x="6.5" y="5" width="3" height="5" fill="var(--on-navy)"/></svg>
        555 210 4877
      </li>
      <li>
        <svg viewBox="0 0 16 16"><circle cx="8" cy="8" r="8" fill="var(--on-navy)"/><rect x="4" y="5" width="8" height="6" fill="var(--navy)"/><path d="M4 5l4 3.5L12 5" fill="none" stroke="var(--on-navy)" stroke-width="0.9"/></svg>
        lena@dorvakel.com
      </li>
    </ul>
  </section>

</body>
</html>
```